Web Design Project

New website for Aged Care business.

Easy buttons to

1.book appointment

2.request a callback

3.view services

think elderly people using it, or family members

we like the colours of 'tall oak' website

and the middle image and call to action buttons of the pods lawncare website.

we'd like a rotating image similar to the pods lawncare but bigger size.

http://www.talloak-example.org.au/

http://www.podslawncare-example.net/

Target Market(s)

elderly people and families of elderly people with enough money to pay for the services offered.

Industry/Entity Type

Business

Requirements
Must have
• contemporary and clean design

```html
<!DOCTYPE html>
<html lang="en">
<head>
<meta charset="utf-8">
<title>Brookfield Care – Aged Care Services</title>
<link rel="stylesheet" href="https://fonts.googleapis.com/css2?family=Source+Sans+3:wght@400;600&display=swap">
<style>
:root{
  --header-bg-top:#f2f1ea;
  --header-bg-bottom:#e6e5dc;
  --page-bg:#ffffff;
  --navy:#2b3590;
  --sky:#29a9e0;
  --sky-light:#4cc6f6;
  --text:#6a6a6a;
  --muted:#7a6a50;
  --footer:#10283f;
  --footer-text:#c9d3dc;
  --frame:#d9d9d9;
}
*{box-sizing:border-box;margin:0;padding:0}
html,body{width:1165px;height:1200px;overflow:hidden}
body{position:relative;background:var(--page-bg);font-family:"Source Sans 3",Arial,sans-serif;color:var(--text)}
.site-header{position:absolute;left:0;top:0;width:1165px;height:139px;background:linear-gradient(var(--header-bg-top),var(--header-bg-bottom))}
.below-header{position:absolute;left:0;top:139px;width:1165px;height:60px;background:linear-gradient(#f6f6f4,#fff)}
.brand{position:absolute;left:47px;top:70px;display:flex;align-items:center;gap:10px;font-size:38px;font-weight:600;color:var(--navy);letter-spacing:-.5px}
.brand-dot{width:14px;height:14px;border-radius:50%;background:var(--sky)}
.call-us{position:absolute;right:55px;top:36px;display:flex;align-items:center;gap:12px;font-size:23px;color:var(--sky)}
.search{position:absolute;left:890px;top:82px;width:220px;height:27px;background:#fff;border:1px solid #cfcfc8;box-shadow:0 1px 2px rgba(0,0,0,.15);font-size:12px;font-style:italic;color:#999;padding:5px 18px}
.search svg{position:absolute;right:8px;top:7px}
.slider{position:absolute;left:58px;top:194px;width:1049px;height:302px;background:var(--frame);border-radius:8px;box-shadow:0 2px 4px rgba(0,0,0,.3)}
.slide{position:absolute;left:7px;top:7px;width:1035px;height:287px;border-radius:6px;overflow:hidden;background:linear-gradient(90deg,#7b746f,#958c84 45%,#a69c92)}
.slide-photo{position:absolute;right:0;top:0;width:590px;height:287px;background:linear-gradient(180deg,#9a8f86 0%,#8a5a4c 45%,#b0282b 75%,#c7302f 100%)}
.slide-caption{position:absolute;left:91px;top:86px;font-size:25px;color:#fff;text-shadow:0 1px 2px rgba(0,0,0,.3)}
.slide-dots{position:absolute;left:91px;top:144px;display:flex;align-items:center;gap:0}
.slide-dots .rule{width:124px;height:1px;background:#fff}
.slide-dots .dot{width:15px;height:15px;border-radius:50%;background:#fff;margin:0 8px}
.slide-dots .dot.active{background:#444;border:2px solid #fff}
.slide-dots .rule:first-child{margin-right:8px}
.slide-dots .rule:last-child{margin-left:8px}
.welcome{position:absolute;left:63px;top:532px;width:748px}
.welcome h1{font-size:23px;font-weight:400;color:var(--navy);margin-bottom:12px}
p{font-size:13.5px;line-height:24.4px;text-align:justify}
.divider{position:absolute;left:63px;top:698px;width:748px;border-top:2px dotted #aaa}
.column{position:absolute;top:723px;width:350px}
.column h2{font-size:19px;font-weight:400;color:var(--sky);margin-bottom:12px}
.column p+p{margin-top:12px}
.column .more{display:block;text-align:right;margin-top:10px;font-size:15px;color:var(--muted)}
.col-left{left:63px}
.col-right{left:452px}
.booking{position:absolute;left:835px;top:535px;width:272px;height:301px;background:linear-gradient(var(--sky-light),var(--sky));border-radius:3px;color:#fff}
.booking h3{position:absolute;left:69px;top:17px;font-size:20px;font-weight:400}
.booking .clock{position:absolute;left:20px;top:10px}
.booking .rule{position:absolute;left:11px;top:59px;width:250px;height:1px;background:rgba(255,255,255,.35)}
.field-label{position:absolute;font-size:12.5px}
.field{position:absolute;height:27px;background:#fff;border:1px solid #9fd8f2;border-radius:2px}
.book-now{position:absolute;left:158px;top:255px;width:97px;height:28px;border-radius:3px;background:linear-gradient(#fff,#d9d9d9);color:#333;font-size:13px;font-weight:600;text-align:center;line-height:28px;box-shadow:0 1px 2px rgba(0,0,0,.3)}
.callback{position:absolute;left:835px;top:851px;width:272px;height:209px;background:linear-gradient(#f6f6f6,#e8e8e8);border:1px solid #e2e2e2;border-radius:2px;overflow:hidden}
.callback-photo{position:absolute;left:0;top:0;width:140px;height:209px;background:linear-gradient(180deg,#e7e3de,#d8c8a8 35%,#eef0f3 70%,#e2e6ec)}
.callback .lead{position:absolute;left:131px;top:49px;font-size:21px;color:#777}
.callback .big{position:absolute;left:131px;top:78px;font-size:30px;color:var(--sky)}
.callback .cta{position:absolute;left:140px;top:125px;width:97px;height:28px;background:linear-gradient(#3fb3e6,#1274a8);color:#fff;font-size:14px;text-align:center;line-height:28px;box-shadow:0 2px 2px rgba(0,0,0,.3)}
.site-footer{position:absolute;left:0;top:1096px;width:1165px;height:104px;background:var(--footer);border-top:2px solid #3a4e62}
.footer-nav{position:absolute;left:61px;top:20px;font-size:12.5px;color:var(--footer-text);display:flex}
.footer-nav span+span::before{content:"|";margin:0 10px}
.copyright{position:absolute;left:61px;top:56px;font-size:12.5px;color:var(--footer-text)}
.social{position:absolute;left:1005px;top:31px;display:flex;gap:9px}
.social span{width:29px;height:29px;border-radius:50%;background:#fff}
</style>
</head>
<body>
<header class="site-header">
  <div class="brand"><span>brightcare</span><span class="brand-dot"></span></div>
  <div class="call-us">
    <svg width="24" height="16" viewBox="0 0 24 16"><path d="M2 6c0-3 4-5 10-5s10 2 10 5l-1 2-4-1-1-2c-3-1-5-1-8 0l-1 2-4 1zM6 9h12l2 6H4z" fill="#29a9e0"/></svg>
    <span>Call us : 555 010 4827</span>
  </div>
  <div class="search">Search
    <svg width="12" height="12" viewBox="0 0 12 12"><circle cx="5" cy="5" r="3.5" fill="none" stroke="#aaa" stroke-width="1.3"/><path d="M7.5 7.5l3.5 3.5" stroke="#aaa" stroke-width="1.5"/></svg>
  </div>
</header>
<div class="below-header"></div>

<section class="slider">
  <div class="slide">
    <div class="slide-photo" role="img" aria-label="Photo of two young carers in red shirts smiling with an elderly woman"></div>
    <div class="slide-caption">Nemo enim ipsam voluptatem quia</div>
    <div class="slide-dots">
      <span class="rule"></span>
      <span class="dot active"></span><span class="dot"></span><span class="dot"></span><span class="dot"></span><span class="dot"></span>
      <span class="rule"></span>
    </div>
  </div>
</section>

<section class="welcome">
  <h1>Welcome to Brookfield Care</h1>
  <p>Sed ut perspiciatis unde omnis iste natus error sit voluptatem accusantium doloremque laudantium, totam rem aperiam, eaque ipsa quae ab illo inventore veritatis et quasi architecto beatae vitae dicta sunt explicabo. Nemo enim ipsam voluptatem quia voluptas sit aspernatur aut odit aut fugit, sed quia consequuntur magni dolores eos qui ratione voluptatem sequi nesciunt.</p>
</section>
<div class="divider"></div>

<article class="column col-left">
  <h2>Care and Support</h2>
  <p>Sed ut perspiciatis unde omnis iste natus error sit voluptatem accusantium doloremque laudantium, totam rem aperiam, eaque ipsa quae ab illo inventore veritatis et quasi architecto beatae vitae dicta sunt explicabo.</p>
  <p>But I must explain to you how all this mistaken idea of denouncing pleasure and praising pain was born and I will give you a complete account of the system, and expound the actual teachings of the great explorer of the truth, the master-builder of human happiness. No one rejects, dislikes, or avoids pleasure itself.</p>
  <a class="more">View more</a>
</article>
<article class="column col-right">
  <h2>Excepteur sint</h2>
  <p>Sed ut perspiciatis unde omnis iste natus error sit voluptatem accusantium doloremque laudantium, totam rem aperiam, eaque ipsa quae ab illo inventore veritatis et quasi architecto beatae vitae dicta sunt explicabo.</p>
  <p>But I must explain to you how all this mistaken idea of denouncing pleasure and praising pain was born and I will give you a complete account of the system, and expound the actual teachings of the great explorer of the truth, the master-builder of human happiness. No one rejects, dislikes, or avoids pleasure itself.</p>
  <a class="more">View more</a>
</article>

<aside class="booking">
  <svg class="clock" width="36" height="38" viewBox="0 0 36 38"><circle cx="7" cy="6" r="4" fill="#e8e8e8"/><circle cx="29" cy="6" r="4" fill="#e8e8e8"/><circle cx="18" cy="21" r="15" fill="#f4f4f4" stroke="#bbb" stroke-width="2"/><path d="M18 12v9l6 4" stroke="#666" stroke-width="2" fill="none"/></svg>
  <h3>Book Appointment</h3>
  <div class="rule"></div>
  <span class="field-label" style="left:35px;top:81px">Name :</span>
  <span class="field" style="left:86px;top:75px;width:170px"></span>
  <span class="field-label" style="left:35px;top:114px">E mail :</span>
  <span class="field" style="left:86px;top:108px;width:170px"></span>
  <span class="field-label" style="left:11px;top:148px">Appointment on :</span>
  <svg style="position:absolute;left:118px;top:145px" width="20" height="18" viewBox="0 0 20 18"><rect x="1" y="2" width="18" height="15" rx="2" fill="#fff" stroke="#1e6f9a"/><rect x="1" y="2" width="18" height="4" fill="#e05a3a"/><rect x="5" y="9" width="3" height="2" fill="#888"/><rect x="10" y="9" width="3" height="2" fill="#888"/><rect x="5" y="13" width="3" height="2" fill="#888"/></svg>
  <span class="field-label" style="left:35px;top:181px">At :</span>
  <span class="field" style="left:86px;top:175px;width:70px"></span>
  <span class="field-label" style="left:166px;top:181px">–</span>
  <span class="field" style="left:185px;top:175px;width:71px"></span>
  <span class="field-label" style="left:35px;top:214px">For :</span>
  <span class="field" style="left:86px;top:208px;width:170px"></span>
  <span class="book-now">BOOK NOW</span>
</aside>

<aside class="callback">
  <div class="callback-photo" role="img" aria-label="Photo of a smiling support agent wearing a headset"></div>
  <span class="lead">Request for</span>
  <span class="big">Callback</span>
  <span class="cta">Click here</span>
</aside>

<footer class="site-footer">
  <nav class="footer-nav">
    <span>Home</span><span>About Us</span><span>Care and Support</span><span>Retirement Living</span><span>Our Locations</span><span>Our Community</span><span>Contact Us</span><span>Sitemap</span>
  </nav>
  <div class="copyright">Copyright © 2012 Brookfield Care &nbsp;&nbsp; All rights reserved.</div>
  <div class="social"><span></span><span></span><span></span></div>
</footer>
</body>
</html>
```